Ember&Willow

I'm writing a book and need a front and back cover for the book.

IMPORTANT DETAILS:
TITLE: Ember & Willow
SUBTITLE: Twelve empowering true stories of women who found strength and hope in times of darkness and despair.
AUTHORS: Marta Pellworth & Dalia Vurnek
1. The book is about WOMEN'S stories of struggle (EMBER) and overcoming them with a hopeful and inspiring story at the end (WILLOW). So the cover of the book should depict these opposing / conflicting ideas.

2. The cover needs to be clean and simple

3. a.The font for the word EMBER should look stronger/bolder/more intense/sturdier/a little more masculine....
b. The ampersand (&) between Ember & Willow should tie the two fonts together
c. The font for the word WILLOW should look fluid/clean/EASY-TO-READ cursive script

4. I'm open to different color fonts with a limit of 3 colors MAX

5. For the back cover: This will be a collection of stories from 12 total authors so the back cover needs to have room for 12 faces somehow.

Looking forward to it.

```html
<!DOCTYPE html>
<html lang="en">
<head>
<meta charset="utf-8">
<title>Ember &amp; Willow — Book Cover</title>
<link rel="stylesheet" href="https://fonts.googleapis.com/css2?family=Graduate&family=Sacramento&family=Cinzel:wght@400;500&family=Montserrat:wght@600&display=swap">
<style>
  :root {
    --backdrop: #a3a3a3;
    --paper: #fbfbf9;
    --ink-grey: #555658;
    --teal: #3aa6a2;
    --band: #2f6f7c;
    --band-text: #ffffff;
    --fig-pink: #f27ab3;
    --fig-yellow: #f7c21c;
    --fig-blue: #1aa2cf;
    --fig-red: #e3202e;
    --fig-dark: #3a2a2d;
    --fig-green: #4dba4a;
    --fig-orange: #f47a20;
    --fig-tan: #d9b267;
  }
  * { box-sizing: border-box; margin: 0; padding: 0; }
  html, body {
    width: 1200px;
    height: 1151px;
    overflow: hidden;
    background: var(--backdrop);
  }
  .cover {
    position: absolute;
    left: 283px;
    top: 100px;
    width: 634px;
    height: 951px;
    background: var(--paper);
    overflow: hidden;
  }
  .title {
    position: absolute;
    left: 0;
    right: 0;
    top: 0;
    height: 370px;
    text-align: center;
    font-weight: normal;
  }
  .title-strong {
    position: absolute;
    left: 0;
    right: 0;
    top: 30px;
    font-family: "Graduate", "Arial Black", sans-serif;
    font-size: 108px;
    line-height: 1;
    letter-spacing: 2px;
    color: var(--ink-grey);
  }
  .title-and {
    position: absolute;
    left: 0;
    right: 0;
    top: 160px;
    font-family: "Montserrat", sans-serif;
    font-weight: 600;
    font-size: 32px;
    line-height: 1;
    letter-spacing: 6px;
    color: var(--ink-grey);
  }
  .title-script {
    position: absolute;
    left: 0;
    right: 0;
    top: 222px;
    font-family: "Sacramento", cursive;
    font-size: 138px;
    line-height: 1;
    color: var(--teal);
    -webkit-text-stroke: 2px var(--teal);
  }
  .subtitle {
    position: absolute;
    left: 30px;
    right: 30px;
    top: 383px;
    font-family: "Cinzel", serif;
    font-size: 16px;
    line-height: 22px;
    letter-spacing: 1.6px;
    text-align: center;
    color: #2c2c2c;
  }
  .artwork {
    position: absolute;
    left: 0;
    right: 0;
    top: 465px;
    bottom: 0;
    background:
      linear-gradient(to bottom, var(--paper) 0%, rgba(251,251,249,0) 35%),
      linear-gradient(to right,
        var(--fig-pink) 0%,
        var(--fig-yellow) 14%,
        var(--fig-blue) 28%,
        var(--fig-dark) 40%,
        var(--fig-red) 52%,
        var(--fig-green) 66%,
        var(--fig-orange) 80%,
        var(--fig-tan) 100%);
  }
  .author-band {
    position: absolute;
    left: 0;
    right: 0;
    top: 883px;
    height: 32px;
    background: var(--band);
    font-family: "Cinzel", serif;
    font-size: 20px;
    line-height: 32px;
    letter-spacing: 2px;
    text-align: center;
    color: var(--band-text);
  }
</style>
</head>
<body>
  <main class="cover">
    <h1 class="title">
      <span class="title-strong">EMBER</span>
      <span class="title-and">AND</span>
      <span class="title-script">Willow</span>
    </h1>
    <p class="subtitle">Twelve empowering true stories of women<br>who found strength and hope in<br>times of darkness and despair.</p>
    <div class="artwork" role="img" aria-label="Illustration of overlapping colourful silhouettes of women raising their arms together"></div>
    <p class="author-band">MARTA PELLWORTH &amp; DALIA VURNEK</p>
  </main>
</body>
</html>
```